Halvorsen Plumbing LLC business card

Would like a modern looking business card with my new logo

Contact Information for Business Card

Dwight Halvorsen 2417 Birchmont Hollow Rd Southbury, CT 06512, Halvorsenplumbingllc@mailnest.example, 203-555-0184

```html
<!DOCTYPE html>
<html lang="en">
<head>
<meta charset="utf-8">
<title>Halvorsen Plumbing LLC — Business Card</title>
<link rel="stylesheet" href="https://fonts.googleapis.com/css2?family=Montserrat:wght@500;600;800&display=swap">
<style>
  :root {
    --backdrop: #3a3a3a;
    --card-black: #1b1b1b;
    --card-black-soft: #2a2a2a;
    --card-white: #ffffff;
    --accent-blue: #1aa7e8;
    --text-light: #ffffff;
    --text-dark: #141414;
  }
  * { margin: 0; padding: 0; box-sizing: border-box; }
  html, body {
    width: 1200px; height: 1200px; overflow: hidden;
    background: var(--backdrop);
    font-family: "Montserrat", Arial, sans-serif;
  }
  .canvas {
    width: 1200px; height: 1200px;
    display: flex; flex-direction: column; align-items: center; justify-content: center;
    gap: 80px;
  }
  .card {
    position: relative;
    width: 720px; height: 412px;
    border-radius: 30px;
    overflow: hidden;
    box-shadow: 0 18px 40px rgba(0,0,0,0.45);
  }
  .card__shapes { position: absolute; inset: 0; width: 100%; height: 100%; }

  /* Front */
  .card--front { background: var(--card-white); }
  .contact {
    position: absolute; left: 50px; top: 132px;
    color: var(--text-light);
    white-space: nowrap;
  }
  .contact__name {
    color: var(--accent-blue);
    font-size: 26px; font-weight: 600; letter-spacing: 0.3px;
    text-transform: uppercase;
    margin-bottom: 16px;
  }
  .contact__list { list-style: none; }
  .contact__item {
    display: flex; align-items: flex-start; gap: 10px;
    font-size: 14px; font-weight: 500; line-height: 1.35;
    margin-bottom: 6px;
  }
  .contact__icon { width: 17px; height: 17px; flex: none; margin-top: 1px; }
  .brand-front {
    position: absolute; left: 500px; top: 150px; width: 200px;
    text-align: center;
    color: var(--text-dark);
    font-size: 22px; font-weight: 800; line-height: 1.15;
    text-transform: uppercase;
  }

  /* Back */
  .card--back {
    background: linear-gradient(115deg, var(--card-black) 0%, var(--card-black-soft) 45%, var(--card-black) 100%);
  }
  .brand-back {
    position: absolute; left: 0; right: 0; top: 130px;
    text-align: center;
    color: var(--text-light);
    font-size: 44px; font-weight: 800; line-height: 1.15;
    text-transform: uppercase;
    letter-spacing: 1px;
  }
  .accent-band {
    position: absolute; right: 0; bottom: 0;
    width: 370px; height: 34px;
    background: var(--accent-blue);
    border-top-left-radius: 26px;
  }
</style>
</head>
<body>
<main class="canvas">

  <section class="card card--front" aria-label="Business card front">
    <svg class="card__shapes" viewBox="0 0 720 412" preserveAspectRatio="none" aria-hidden="true">
      <polygon points="0,0 285,0 470,230 520,412 0,412" fill="var(--card-black)"/>
      <polyline points="297,0 482,230 532,412" fill="none" stroke="var(--accent-blue)" stroke-width="5"/>
    </svg>

    <div class="contact">
      <h1 class="contact__name">Dwight Halvorsen</h1>
      <ul class="contact__list">
        <li class="contact__item">
          <svg class="contact__icon" viewBox="0 0 24 24" aria-hidden="true"><path fill="var(--accent-blue)" d="M6.6 10.8a15.1 15.1 0 0 0 6.6 6.6l2.2-2.2a1 1 0 0 1 1-.25 11.4 11.4 0 0 0 3.6.6 1 1 0 0 1 1 1V20a1 1 0 0 1-1 1A17 17 0 0 1 3 4a1 1 0 0 1 1-1h3.5a1 1 0 0 1 1 1c0 1.250.2 2.450.6 3.6a1 1 0 0 1-.25 1z"/></svg>
          <span>203-555-0184</span>
        </li>
        <li class="contact__item">
          <svg class="contact__icon" viewBox="0 0 24 24" aria-hidden="true"><path fill="var(--accent-blue)" d="M2 5h20v14H2z"/><path d="M2 5l10 8 10-8" fill="none" stroke="var(--card-black)" stroke-width="1.8"/></svg>
          <span>Halvorsenplumbingllc@mailnest.example</span>
        </li>
        <li class="contact__item">
          <svg class="contact__icon" viewBox="0 0 24 24" aria-hidden="true"><path fill="var(--accent-blue)" d="M12 2a7 7 0 0 0-7 7c0 5.2 7 13 7 13s7-7.8 7-13a7 7 0 0 0-7-7zm0 9.5A2.5 2.5 0 1 1 12 6.5a2.5 2.5 0 0 1 0 5z"/></svg>
          <span>2417 Birchmont Hollow Rd<br>Southbury, CT 06512</span>
        </li>
      </ul>
    </div>

    <p class="brand-front">Halvorsen Plumbing LLC</p>
  </section>

  <section class="card card--back" aria-label="Business card back">
    <p class="brand-back">Halvorsen<br>Plumbing LLC</p>
    <div class="accent-band" aria-hidden="true"></div>
  </section>

</main>
</body>
</html>
```